looking to create a Bridal Nest List with our logo and input the items on our list. I attached an example of what I'm looking for. Need to be similar and on nice stationary wedding paper. Simple and Elegant. Put 15% off orders.

```html
<!DOCTYPE html>
<html lang="en">
<head>
<meta charset="utf-8">
<title>Bridal Nest Registry – Wedding Registry Checklist</title>
<link rel="stylesheet" href="https://fonts.googleapis.com/css2?family=Cormorant+Garamond:wght@600&family=Open+Sans:wght@400&family=Montserrat:wght@700&display=swap">
<style>
  :root{
    --paper:#f2f0ea;
    --frame:#d6cf2c;
    --purple:#8d6aa9;
    --olive:#b2ad25;
    --ink:#4a4a4a;
    --ink-dark:#2e2e2e;
    --logo-bg:#e9e7e2;
  }
  *{box-sizing:border-box;margin:0;padding:0}
  html,body{width:723px;height:1200px;overflow:hidden;background:var(--paper)}
  .sheet{position:relative;width:723px;height:1200px;background:var(--paper);border:7px solid var(--frame);overflow:hidden}
  .floral{position:absolute}
  .floral--top{left:-7px;top:-7px;width:400px;height:340px}
  .floral--bottom{right:-7px;bottom:-7px;width:350px;height:310px}

  .brand{position:absolute;left:405px;top:60px;width:272px;height:120px;background:var(--logo-bg);display:flex;align-items:center;justify-content:center}
  .brand__name{font-family:"Cormorant Garamond",serif;font-weight:600;font-size:34px;line-height:1;color:var(--ink-dark);text-align:center}

  .title{position:absolute;left:190px;top:228px;width:500px;text-align:center;white-space:nowrap;font-family:"Cormorant Garamond",serif;font-weight:600;font-size:31px;letter-spacing:0;color:var(--purple);text-transform:uppercase}

  .heading{position:absolute;display:flex;align-items:center;gap:8px;white-space:nowrap;font-family:"Cormorant Garamond",serif;font-weight:600;font-size:29px;color:var(--olive);text-transform:uppercase}
  .heading svg{width:24px;height:24px}
  .heading--pharmacy{left:265px;top:338px}
  .heading--stationary{left:82px;top:740px}
  .heading--misc{left:400px;top:740px}

  .list{position:absolute;list-style:none;font-family:"Open Sans",sans-serif;font-size:14px;line-height:17px;color:var(--ink)}
  .list li{position:relative;padding-left:20px;margin-bottom:9px}
  .list li::before{content:"";position:absolute;left:0;top:4px;width:9px;height:9px;border:1.5px solid var(--purple)}
  .list small{display:block;font-size:11px;line-height:13px}
  .list small.inline{display:inline}
  .list--c1{left:40px;top:412px;width:205px}
  .list--c2{left:265px;top:412px;width:210px}
  .list--c3{left:487px;top:412px;width:205px}
  .list--s1{left:40px;top:800px;width:180px}
  .list--s2{left:227px;top:800px;width:150px}
  .list--m1{left:400px;top:800px;width:150px}
  .list--m2{left:547px;top:800px;width:150px}

  .offer{position:absolute;left:2px;bottom:2px;width:165px;height:118px;background:var(--purple);clip-path:polygon(0 0,85% 0,100% 50%,85% 100%,0 100%);color:#fff;font-family:"Cormorant Garamond",serif;font-weight:600;display:flex;align-items:center;padding-left:14px}
  .offer__num{font-size:70px;line-height:1}
  .offer__pct{display:flex;flex-direction:column;line-height:.9;margin-left:2px}
  .offer__pct b{font-size:34px;font-weight:600}
  .offer__pct span{font-size:26px}
  .offer-text{position:absolute;left:182px;bottom:30px;font-family:"Montserrat",sans-serif;font-weight:700;font-size:25px;line-height:26px;color:var(--ink-dark);text-transform:uppercase}
</style>
</head>
<body>
<main class="sheet">
  <svg class="floral floral--top" viewBox="0 0 400 340" role="img" aria-label="Watercolour floral corner with coral and pink blossoms and green leaves">
    <defs>
      <radialGradient id="bloomTop" cx="35%" cy="30%" r="70%">
        <stop offset="0" stop-color="#f29a8f"/>
        <stop offset=".55" stop-color="#e6b2a4"/>
        <stop offset="1" stop-color="#a9c4ad" stop-opacity=".55"/>
      </radialGradient>
    </defs>
    <path d="M0 0H400C390 60 350 110 300 130C250 150 200 170 150 200C100 230 60 280 30 340H0Z" fill="url(#bloomTop)"/>
  </svg>
  <svg class="floral floral--bottom" viewBox="0 0 350 310" role="img" aria-label="Watercolour floral corner with coral blossoms, grey and green leaves">
    <defs>
      <radialGradient id="bloomBottom" cx="65%" cy="70%" r="70%">
        <stop offset="0" stop-color="#f0928a"/>
        <stop offset=".55" stop-color="#e4b3a6"/>
        <stop offset="1" stop-color="#a8bfae" stop-opacity=".55"/>
      </radialGradient>
    </defs>
    <path d="M350 0V310H0C40 270 90 240 140 220C200 195 250 150 290 90C315 55 335 25 350 0Z" fill="url(#bloomBottom)"/>
  </svg>

  <div class="brand">
    <span class="brand__name">Bridal Nest<br>Registry</span>
  </div>

  <h1 class="title">Wedding Registry Checklist</h1>

  <h2 class="heading heading--pharmacy">
    <svg viewBox="0 0 26 26" aria-hidden="true"><circle cx="9" cy="16" r="7" fill="var(--purple)"/><rect x="12" y="3" width="9" height="16" rx="4.5" transform="rotate(35 16 11)" fill="var(--purple)"/></svg>
    Pharmacy
  </h2>
  <ul class="list list--c1">
    <li>Hair Products (Hairspray; Mousse; Gel; curlers)</li>
    <li>Shampoo and conditioner</li>
    <li>Body Soap</li>
    <li>Powder</li>
    <li>Deodorant</li>
    <li>Toothbrush</li>
    <li>Toothpaste</li>
    <li>Mouthwash</li>
    <li>Dental Floss</li>
  </ul>
  <ul class="list list--c2">
    <li>Allergy Medicine<small>(Allerease; Zyrocal; Clarivo; Allevia)</small></li>
    <li>Cotton swabs</li>
    <li>Lotions; Creams;</li>
    <li>Facial Wash</li>
    <li>Cotton Balls/Pads</li>
    <li>Thermometer</li>
    <li>Antifungal cream/powder</li>
    <li>Sanitary Napkins</li>
    <li>Cold Remedy medicine<small>(Painova Cold; Mucolin)</small></li>
  </ul>
  <ul class="list list--c3">
    <li>His and Hers Vitamins</li>
    <li>Analgesics <small class="inline">(Painova; Motrex; Advina; Etc.)</small></li>
    <li>Bandages</li>
    <li>Bacitracin or Neomend</li>
    <li>Peroxide</li>
    <li>Rubbing alcohol</li>
    <li>Nail Clipper or Scissors</li>
    <li>Lens Solution; Rewetting Drops</li>
    <li>Lubricants <small class="inline">(SL; Silkaglide; Etc.)</small></li>
  </ul>

  <h2 class="heading heading--stationary">
    <svg viewBox="0 0 26 26" aria-hidden="true"><circle cx="9" cy="15" r="6.5" fill="none" stroke="var(--purple)" stroke-width="2.5"/><circle cx="17" cy="15" r="6.5" fill="none" stroke="var(--purple)" stroke-width="2.5"/></svg>
    Stationary
  </h2>
  <ul class="list list--s1">
    <li>Pens; Pencils; Markers</li>
    <li>Writing Pads</li>
    <li>Tape</li>
  </ul>
  <ul class="list list--s2">
    <li>Scissors</li>
    <li>Envelopes</li>
  </ul>

  <h2 class="heading heading--misc">
    <svg viewBox="0 0 26 26" aria-hidden="true"><circle cx="9" cy="6" r="4" fill="var(--purple)"/><path d="M3 24V14a6 6 0 0 1 12 0v10Z" fill="var(--purple)"/><rect x="14" y="14" width="10" height="9" fill="var(--purple)"/></svg>
    Miscellaneous
  </h2>
  <ul class="list list--m1">
    <li>Umbrellas</li>
    <li>Rain Bonnet</li>
    <li>Hat Protectors</li>
    <li>Batteries</li>
  </ul>
  <ul class="list list--m2">
    <li>Sewing Kits</li>
    <li>Air Fresheners</li>
    <li>Cleaning Wipes</li>
    <li>Safety Pins</li>
  </ul>

  <div class="offer">
    <span class="offer__num">15</span>
    <span class="offer__pct"><b>%</b><span>OFF</span></span>
  </div>
  <p class="offer-text">All Bridal Nest<br>Orders</p>
</main>
</body>
</html>
```